Web Based Ordering. We have an existing input screen- Need to Clean it up

we have an existing ordering Modal on a trucking management system, but it looks and feels clunky. We would like to modernize the look and feel of it. We need to keep the same input fields, but we are open to any type of reconfiguration or layout changes you can think of to improve the flow and layout.

This design is for a web browser, not mobile app.

Target Market(s)

construction and trucking industry

Colors
85acd3
3176b5
33a6d7
85cae6
33b8a4
86cfc6

Requirements
Must have
• all the input fields displayed are required
Nice to have
• some of the fields can probably be combined to consolidate the number of tabs.

```html
<!DOCTYPE html>
<html lang="en">
<head>
<meta charset="utf-8">
<title>New Material Order</title>
<link href="https://fonts.googleapis.com/css2?family=Lato:wght@400;700&display=swap" rel="stylesheet">
<style>
:root{
  --page:#ffffff;
  --board:#ececec;
  --header:#2762a6;
  --card:#ffffff;
  --ink:#1f1f1f;
  --text:#333333;
  --border:#cfcfcf;
  --rule:#d6d6d6;
  --teal:#2aa88f;
  --teal-text:#2aa394;
  --blue:#2d8fd2;
  --req:#33a6d7;
  --dark:#3d3d3d;
  --note:#3176b5;
}
*{box-sizing:border-box;margin:0;padding:0}
html,body{width:1200px;height:2244px;overflow:hidden;background:var(--page)}
body{font-family:'Lato',sans-serif;color:var(--text)}
.stage{position:absolute;left:0;top:0;width:1380px;height:2580px;transform:scale(0.869565);transform-origin:0 0}
.board{position:absolute;left:92px;top:32px;width:1194px;height:2480px;background:var(--board)}
.order{position:absolute;left:166px;width:1047px}
.order-header{position:absolute;left:0;top:0;width:1047px;height:67px;background:var(--header);border-radius:3px;color:#fff;font-weight:700;font-size:22px;line-height:67px;padding-left:24px}
.order-card{position:absolute;left:0;top:81px;width:1047px;background:var(--card)}
.tab{position:absolute;font-size:17px;line-height:22px;color:var(--ink);font-weight:700;white-space:nowrap}
.tab.done,.tab.active{color:var(--teal-text);font-weight:400}
.tab svg{position:absolute;left:-32px;top:2px}
.tab-rule{position:absolute;left:0;width:1047px;height:1px;background:var(--rule)}
.tab-marker{position:absolute;height:8px;background:var(--blue)}
.edit-icon{position:absolute;left:997px}
.label{position:absolute;font-size:17px;font-weight:700;line-height:22px;color:var(--ink)}
.label .req{color:var(--req);font-weight:400}
.field{position:absolute;height:56px;border:1px solid var(--border);border-radius:3px;background:#fff;font-size:15px;line-height:54px;padding-left:23px;color:var(--text)}
.field .clear{position:absolute;right:30px;top:0;font-size:15px;color:var(--ink)}
.field .clear.solo{right:24px}
.field .caret{position:absolute;right:20px;top:25px}
.outline-btn{position:absolute;left:25px;width:217px;height:56px;border:2px solid var(--teal);border-radius:3px;color:var(--teal-text);font-weight:700;font-size:15px;line-height:52px;text-align:center;background:#fff}
.toggle{position:absolute;left:25px;width:217px;height:56px;display:flex;border:2px solid var(--blue);border-radius:3px;overflow:hidden;font-size:17px;font-weight:700}
.toggle span{display:block;line-height:52px;text-align:center}
.toggle .off{width:100px;color:var(--blue);background:#fff}
.toggle .on{flex:1;color:#fff;background:var(--blue)}
.btn{position:absolute;width:130px;height:50px;border-radius:3px;color:#fff;font-weight:700;font-size:18px;line-height:50px;text-align:center}
.btn-cancel{left:379px;background:var(--dark)}
.btn-continue{left:539px;background:var(--teal)}
.btn-continue svg{vertical-align:-1px;margin-left:4px}
.scale-note{position:absolute;left:1253px;font-size:14px;color:var(--note)}
.outside-clear{position:absolute;left:1194px;font-size:15px;font-weight:700;color:var(--ink)}
</style>
</head>
<body>
<div class="stage">
  <div class="board"></div>

  <!-- Step 1: Date and Start -->
  <section class="order" style="top:81px">
    <div class="order-header">New Material Order</div>
    <div class="order-card" style="height:548px">
      <span class="tab done" style="left:62px;top:30px"><svg width="20" height="16" viewBox="0 0 20 16"><path d="M2 8l5 5L18 2" fill="none" stroke="#2aa394" stroke-width="3"/></svg>Date and Start</span>
      <span class="tab done" style="left:278px;top:30px"><svg width="20" height="16" viewBox="0 0 20 16"><path d="M2 8l5 5L18 2" fill="none" stroke="#2aa394" stroke-width="3"/></svg>Destination</span>
      <span class="tab" style="left:442px;top:30px">Material</span>
      <span class="tab done" style="left:611px;top:30px"><svg width="20" height="16" viewBox="0 0 20 16"><path d="M2 8l5 5L18 2" fill="none" stroke="#2aa394" stroke-width="3"/></svg>Trucks</span>
      <span class="tab done" style="left:765px;top:30px"><svg width="20" height="16" viewBox="0 0 20 16"><path d="M2 8l5 5L18 2" fill="none" stroke="#2aa394" stroke-width="3"/></svg>Rates</span>
      <span class="tab" style="left:881px;top:30px">Summary</span>
      <svg class="edit-icon" style="top:32px" width="18" height="18" viewBox="0 0 18 18"><path d="M2 16l1-5L13 1l4 4L7 15z" fill="#1f1f1f"/></svg>
      <div class="tab-rule" style="top:76px"></div>
      <div class="tab-marker" style="left:19px;width:167px;top:72px"></div>

      <div class="label" style="left:28px;top:107px">Customer<span class="req">*</span></div>
      <div class="field" style="left:25px;top:141px;width:997px">R.T. Halvorsen Paving Group, Inc.<span class="clear">x</span><svg class="caret" width="10" height="6" viewBox="0 0 10 6"><path d="M0 0h10L5 6z" fill="#1f1f1f"/></svg></div>

      <div class="label" style="left:28px;top:214px">Starting Location<span class="req">*</span></div>
      <div class="field" style="left:25px;top:248px;width:997px">2109-Ridgeway County Rd 7<span class="clear">x</span><svg class="caret" width="10" height="6" viewBox="0 0 10 6"><path d="M0 0h10L5 6z" fill="#1f1f1f"/></svg></div>

      <div class="label" style="left:28px;top:318px">Load Date<span class="req">*</span></div>
      <div class="field" style="left:25px;top:352px;width:484px">02/27/2021<span class="clear solo">x</span></div>
      <div class="label" style="left:541px;top:318px">Load Time<span class="req">*</span></div>
      <div class="field" style="left:539px;top:352px;width:484px">6:00 AM<span class="clear solo">x</span></div>

      <div class="btn btn-cancel" style="top:439px">Cancel</div>
      <div class="btn btn-continue" style="top:439px">Continue<svg width="9" height="13" viewBox="0 0 9 13"><path d="M2 1l5 5.5L2 12" fill="none" stroke="#fff" stroke-width="2.2"/></svg></div>
    </div>
  </section>
  <div class="scale-note" style="top:741px">x10</div>

  <!-- Step 2: Destination -->
  <section class="order" style="top:816px">
    <div class="order-header">New Material Order</div>
    <div class="order-card" style="height:830px">
      <span class="tab done" style="left:62px;top:29px"><svg width="20" height="16" viewBox="0 0 20 16"><path d="M2 8l5 5L18 2" fill="none" stroke="#2aa394" stroke-width="3"/></svg>Date and Start</span>
      <span class="tab done" style="left:278px;top:29px"><svg width="20" height="16" viewBox="0 0 20 16"><path d="M2 8l5 5L18 2" fill="none" stroke="#2aa394" stroke-width="3"/></svg>Destination</span>
      <span class="tab" style="left:442px;top:29px">Material</span>
      <span class="tab done" style="left:611px;top:29px"><svg width="20" height="16" viewBox="0 0 20 16"><path d="M2 8l5 5L18 2" fill="none" stroke="#2aa394" stroke-width="3"/></svg>Trucks</span>
      <span class="tab done" style="left:765px;top:29px"><svg width="20" height="16" viewBox="0 0 20 16"><path d="M2 8l5 5L18 2" fill="none" stroke="#2aa394" stroke-width="3"/></svg>Rates</span>
      <span class="tab" style="left:881px;top:29px">Summary</span>
      <svg class="edit-icon" style="top:31px" width="18" height="18" viewBox="0 0 18 18"><path d="M2 16l1-5L13 1l4 4L7 15z" fill="#1f1f1f"/></svg>
      <div class="tab-rule" style="top:75px"></div>
      <div class="tab-marker" style="left:224px;width:167px;top:71px"></div>

      <div class="label" style="left:28px;top:106px">PO /Job#</div>
      <div class="field" style="left:25px;top:141px;width:484px">12<span class="clear">x</span></div>
      <div class="label" style="left:541px;top:106px">Destination*</div>
      <div class="field" style="left:539px;top:141px;width:484px">RHP Plant 12- Millbrook<span class="clear">x</span></div>

      <div class="label" style="left:28px;top:214px">Address <span class="req">*</span></div>
      <div class="field" style="left:25px;top:248px;width:997px">1480 Foundry Park Drive , Millbrook, GA, 30190</div>

      <div class="label" style="left:28px;top:318px">Job Site Contact<span class="req">*</span></div>
      <div class="field" style="left:25px;top:352px;width:484px;padding-left:19px">Dale Maren<span class="clear" style="right:40px">x</span><svg class="caret" width="10" height="6" viewBox="0 0 10 6"><path d="M0 0h10L5 6z" fill="#1f1f1f"/></svg></div>
      <div class="label" style="left:541px;top:318px">Contact Number<span class="req">*</span></div>
      <div class="field" style="left:539px;top:352px;width:484px">(555) 014-2260</div>

      <div class="outline-btn" style="top:423px">+ Add Second Destination</div>

      <div class="label" style="left:28px;top:497px">Billing Job Site<span class="req">*</span></div>
      <div class="field" style="left:25px;top:531px;width:484px;padding-left:19px">2109-Ridgeway County Rd 7<svg class="caret" width="10" height="6" viewBox="0 0 10 6"><path d="M0 0h10L5 6z" fill="#1f1f1f"/></svg></div>
      <div class="label" style="left:541px;top:497px">Phase Code <span class="req">*</span></div>
      <div class="field" style="left:539px;top:531px;width:484px">01. 0015., FIELD EN x<span class="clear">x</span><svg class="caret" width="10" height="6" viewBox="0 0 10 6"><path d="M0 0h10L5 6z" fill="#1f1f1f"/></svg></div>

      <div class="label" style="left:28px;top:605px">Prevailing Wage?</div>
      <div class="toggle" style="top:637px"><span class="off">Yes</span><span class="on">No</span></div>

      <div class="btn btn-cancel" style="top:728px">Cancel</div>
      <div class="btn btn-continue" style="top:728px">Continue<svg width="9" height="13" viewBox="0 0 9 13"><path d="M2 1l5 5.5L2 12" fill="none" stroke="#fff" stroke-width="2.2"/></svg></div>
    </div>
  </section>
  <div class="scale-note" style="top:1712px">x10</div>

  <!-- Step 3: Material -->
  <section class="order" style="top:1826px">
    <div class="order-header">New Material Order</div>
    <div class="order-card" style="height:548px">
      <span class="tab done" style="left:62px;top:30px"><svg width="20" height="16" viewBox="0 0 20 16"><path d="M2 8l5 5L18 2" fill="none" stroke="#2aa394" stroke-width="3"/></svg>Date and Start</span>
      <span class="tab done" style="left:278px;top:30px"><svg width="20" height="16" viewBox="0 0 20 16"><path d="M2 8l5 5L18 2" fill="none" stroke="#2aa394" stroke-width="3"/></svg>Destination</span>
      <span class="tab active" style="left:442px;top:30px">Material</span>
      <span class="tab done" style="left:611px;top:30px"><svg width="20" height="16" viewBox="0 0 20 16"><path d="M2 8l5 5L18 2" fill="none" stroke="#2aa394" stroke-width="3"/></svg>Trucks</span>
      <span class="tab done" style="left:765px;top:30px"><svg width="20" height="16" viewBox="0 0 20 16"><path d="M2 8l5 5L18 2" fill="none" stroke="#2aa394" stroke-width="3"/></svg>Rates</span>
      <span class="tab" style="left:881px;top:30px">Summary</span>
      <svg class="edit-icon" style="top:32px" width="18" height="18" viewBox="0 0 18 18"><path d="M2 16l1-5L13 1l4 4L7 15z" fill="#1f1f1f"/></svg>
      <div class="tab-rule" style="top:76px"></div>
      <div class="tab-marker" style="left:401px;width:139px;top:72px"></div>

      <div class="label" style="left:28px;top:107px">Work Type<span class="req">*</span></div>
      <div class="field" style="left:25px;top:141px;width:997px">Asphalt — Machine Paving<span class="clear">x</span><svg class="caret" width="10" height="6" viewBox="0 0 10 6"><path d="M0 0h10L5 6z" fill="#1f1f1f"/></svg></div>

      <div class="label" style="left:28px;top:214px">Material Type<span class="req">*</span></div>
      <div class="field" style="left:25px;top:248px;width:484px">12.5mm PEM<span class="clear solo">x</span></div>
      <div class="label" style="left:538px;top:214px">Tonnage<span class="req">*</span></div>
      <div class="field" style="left:539px;top:248px;width:484px">400<svg style="position:absolute;right:22px;top:21px" width="8" height="13" viewBox="0 0 8 13"><path d="M0 5h8L4 0zM0 8h8L4 13z" fill="#1f1f1f"/></svg></div>

      <div class="outline-btn" style="top:318px">+ Additional Material</div>

      <div class="btn btn-cancel" style="top:439px">Cancel</div>
      <div class="btn btn-continue" style="top:439px">Continue<svg width="9" height="13" viewBox="0 0 9 13"><path d="M2 1l5 5.5L2 12" fill="none" stroke="#fff" stroke-width="2.2"/></svg></div>
    </div>
  </section>
  <div class="outside-clear" style="top:2174px">x</div>
  <div class="scale-note" style="top:2487px">x10</div>
</div>
</body>
</html>
```